verdant terraces simple classy business card design

my name is owen harlow and I run a gardening business aimed at high class verdant terraces. the business name is verdant terraces and our logo was designed on pixel forum .My clientel are anything from residential homes to businesses. I take pride in my work and know that I offer a service like no other in my area.
The business card will be used to represent my business and I want it to be not only rememberable, but simplistic and modern. Eye catching too. Of course I would like it relatable to gardening and appealing to the correct clientel - those being garden enthusiasts, prestigious homes and businesses that are after top of the line gardening services like no other on the market.
I am not a typical lawn mowing business so I don't want a typical card design that represents that. The gardens I work with are generally million dollar properties with owners who are very garden proud looking for upkeep and guidance from me along with sometimes whole new garden designs. I want the business cards to show to my clients that I take pride, as they do, in their garden. And I want them to know from my card that I am a professional, qualified horticulturist offering them a top of the line service for life. I want them to refer my business on. I want them to look at my business card and see class and professionalism in a modern unique bold way.
The card should be simple with the possibility of the logo on the front being embossed/debossed and my details on the back the card should have a organic garden feel it's very important to me that it is absolutely perfect
I am also very open to ideas and suggestions so look forward to seeing the designs. the business logo has been supplied with this project and I want the card to be double sided

Contact info is
Owen Harlow - Managing Director / Horticulturist
Phone : 0481 526 704
Email: owenharlow@verdantterraces.com.au

Target Market(s)

high class gardens residential and commercial

Industry/Entity Type

Gardener

Contact Information for Business Card

Contact info is
Phone : 0481 526 704

PLEASE MAKE CARD DOUBLE SIDED

Requirements
Must have
• organic simple classy modern feel
• must flow with the current logo that has been supplied with this project
• Double sided
• Must explain in a simple way that I deal with high end gardens and I'm a qualified horticulturist
Nice to have
• embossed debossed logo
Should not have
• shouldn't be to busy or cheap looking

```html
<!DOCTYPE html>
<html lang="en">
<head>
<meta charset="utf-8">
<title>Verdant Terraces – Business Card</title>
<link href="https://fonts.googleapis.com/css2?family=Open+Sans:wght@400;600&display=swap" rel="stylesheet">
<style>
  :root {
    --stage: #e4e6e9;
    --charcoal: #2e2e30;
    --charcoal-soft: #3b3b3d;
    --leaf: #6cb83f;
    --leaf-light: #86c95a;
    --leaf-dark: #4f9a2c;
    --paper: #ffffff;
    --rule: #b9b9bb;
    --ink: #1d1d1f;
    --muted: #dcdcdc;
  }
  * { margin: 0; padding: 0; box-sizing: border-box; }
  html, body { width: 1200px; height: 800px; overflow: hidden; }
  body {
    background: var(--stage);
    font-family: "Open Sans", Arial, sans-serif;
    display: flex;
    align-items: center;
    justify-content: center;
    gap: 60px;
  }
  .card {
    position: relative;
    width: 520px;
    height: 300px;
    border-radius: 4px;
    overflow: hidden;
    box-shadow: 0 10px 28px rgba(0,0,0,.18);
  }
  .card-art { position: absolute; inset: 0; width: 100%; height: 100%; }

  /* Front */
  .front-brand {
    position: absolute;
    left: 50%;
    top: 100px;
    transform: translateX(-50%);
    display: flex;
    align-items: center;
    gap: 10px;
    white-space: nowrap;
    color: var(--paper);
  }
  .brand-dot {
    width: 20px; height: 20px;
    border-radius: 50%;
    background: var(--paper);
    flex: none;
  }
  .brand-name {
    font-weight: 600;
    font-size: 20px;
    letter-spacing: 3px;
    text-transform: uppercase;
    line-height: 1;
  }

  /* Back */
  .back-brand {
    position: absolute;
    left: 34px; top: 26px;
    display: flex; align-items: center; gap: 8px;
    white-space: nowrap;
    color: var(--leaf);
  }
  .back-brand .brand-dot { width: 16px; height: 16px; background: var(--leaf); }
  .back-brand .brand-name { font-size: 17px; letter-spacing: 2px; }
  .holder { position: absolute; left: 34px; top: 68px; }
  .holder-name {
    color: var(--leaf);
    font-weight: 600;
    font-size: 19px;
    text-transform: uppercase;
    letter-spacing: .5px;
  }
  .holder-role {
    color: var(--muted);
    font-size: 11.5px;
    font-variant: small-caps;
    line-height: 1.35;
    margin-top: 2px;
  }
  .address {
    position: absolute;
    left: 24px; bottom: 60px;
    display: flex; align-items: center; gap: 10px;
    color: var(--paper);
    font-size: 13px;
    text-transform: uppercase;
  }
  .pin { width: 24px; height: 24px; }
  .contacts {
    position: absolute;
    right: 22px; top: 168px;
    list-style: none;
    display: flex; flex-direction: column; gap: 6px;
  }
  .contact {
    display: flex; align-items: center; justify-content: flex-end; gap: 10px;
    color: var(--ink);
    font-size: 12.5px;
    white-space: nowrap;
  }
  .contact-phone { font-size: 16px; letter-spacing: .5px; }
  .contact-icon { width: 24px; height: 24px; flex: none; }
</style>
</head>
<body>

  <section class="card card-front" aria-label="Card front">
    <svg class="card-art" viewBox="0 0 520 300" preserveAspectRatio="none" aria-hidden="true">
      <rect width="520" height="300" fill="var(--paper)"/>
      <polygon points="0,0 230,0 520,110 520,250 0,130" fill="var(--leaf)"/>
      <polygon points="0,0 230,0 520,110 520,135 0,25" fill="var(--leaf-light)" opacity=".5"/>
      <polygon points="0,130 520,250 520,300 0,300" fill="var(--charcoal)"/>
    </svg>
    <div class="front-brand">
      <span class="brand-dot"></span>
      <span class="brand-name">Verdant Terraces</span>
    </div>
  </section>

  <section class="card card-back" aria-label="Card back">
    <svg class="card-art" viewBox="0 0 520 300" preserveAspectRatio="none" aria-hidden="true">
      <rect width="520" height="300" fill="var(--charcoal)"/>
      <polygon points="0,0 520,0 520,120 0,175" fill="var(--charcoal-soft)" opacity=".5"/>
      <polygon points="110,163 520,120 520,300 380,300" fill="var(--rule)"/>
      <polygon points="120,166 520,126 520,300 380,300" fill="var(--paper)"/>
      <polygon points="0,170 110,163 380,300 0,300" fill="var(--leaf)"/>
      <polygon points="0,190 95,175 330,300 0,300" fill="var(--leaf-light)"/>
      <polygon points="110,163 380,300 365,300 100,168" fill="var(--leaf-dark)"/>
    </svg>

    <div class="back-brand">
      <span class="brand-dot"></span>
      <span class="brand-name">Verdant Terraces</span>
    </div>
    <div class="holder">
      <p class="holder-name">Owen Harlow</p>
      <p class="holder-role">Managing Director /<br>Horticulturist</p>
    </div>

    <p class="address">
      <svg class="pin" viewBox="0 0 24 24" aria-hidden="true">
        <circle cx="12" cy="12" r="12" fill="var(--charcoal)"/>
        <path d="M12 5a4.5 4.5 0 0 0-4.5 4.5c0 3.2 4.5 8.5 4.5 8.5s4.5-5.3 4.5-8.5A4.5 4.5 0 0 0 12 5z" fill="var(--paper)"/>
        <circle cx="12" cy="9.5" r="1.7" fill="var(--charcoal)"/>
      </svg>
      Supply Address
    </p>

    <ul class="contacts">
      <li class="contact contact-phone">0481 526 704
        <svg class="contact-icon" viewBox="0 0 24 24" aria-hidden="true">
          <circle cx="12" cy="12" r="12" fill="var(--leaf)"/>
          <path d="M8.5 6.5l2 2.5-1.2 1.3c.7 1.6 2 2.9 3.5 3.6l1.3-1.2 2.5 2-1.2 1.8c-4.2-.4-7.9-4.1-8.3-8.3z" fill="var(--paper)"/>
        </svg>
      </li>
      <li class="contact">owenharlow@verdantterraces.com.au
        <svg class="contact-icon" viewBox="0 0 24 24" aria-hidden="true">
          <circle cx="12" cy="12" r="12" fill="var(--leaf)"/>
          <rect x="6" y="8" width="12" height="8.5" fill="var(--paper)"/>
          <path d="M6 8l6 5 6-5" fill="none" stroke="var(--leaf)" stroke-width="1.2"/>
        </svg>
      </li>
      <li class="contact">www.verdantterraces.com
        <svg class="contact-icon" viewBox="0 0 24 24" aria-hidden="true">
          <circle cx="12" cy="12" r="12" fill="var(--leaf)"/>
          <g fill="none" stroke="var(--paper)" stroke-width="1.2">
            <circle cx="12" cy="12" r="6"/>
            <ellipse cx="12" cy="12" rx="2.6" ry="6"/>
            <line x1="6" y1="12" x2="18" y2="12"/>
            <line x1="7" y1="9" x2="17" y2="9"/>
            <line x1="7" y1="15" x2="17" y2="15"/>
          </g>
        </svg>
      </li>
    </ul>
  </section>

</body>
</html>
```